Quorvex business card design

create modern and tech looking business card that is clean but effectively communciates that we are a cloud communications company.
Should have at minimum:
Employee Name
Postion
Phone Number
Email
website
create modern and tech looking business card that is clean but effectively communciates that we are a cloud communications company. We have two logo color schemes (attached) so would like to see designs both ways
Should have at minimum:
Employee Name
Postion
Phone Number
Email
website

```html
<!DOCTYPE html>
<html lang="en">
<head>
<meta charset="utf-8">
<title>Quorvex business card</title>
<link rel="stylesheet" href="https://fonts.googleapis.com/css2?family=Arimo:wght@400;700&family=Tinos&display=swap">
<style>
  :root {
    --backdrop: #e4e4e4;
    --card: #000000;
    --accent-blue: #3d9ad9;
    --accent-cyan: #55f2e0;
    --text-grey: #c2c2c2;
    --wordmark-grey: #b5b5b5;
  }
  * { margin: 0; padding: 0; box-sizing: border-box; }
  html, body {
    width: 1200px; height: 1200px; overflow: hidden;
    background: var(--backdrop);
  }
  .canvas { position: relative; width: 1200px; height: 1200px; }
  .card {
    position: absolute; left: 180px; width: 840px; height: 480px;
    background: var(--card); border-radius: 24px; overflow: hidden;
  }
  .card--front { top: 111px; }
  .card--back { top: 610px; }
  .card-backdrop {
    position: absolute; inset: 0;
    background:
      radial-gradient(ellipse 62% 58% at 60% 50%, var(--card) 45%, rgba(0,0,0,0) 100%),
      linear-gradient(100deg, var(--accent-blue) 0%, #1f5f8c 35%, #0d2c44 70%, #1f5f8c 100%);
  }

  .wordmark {
    position: absolute; display: flex; align-items: center;
    font-family: "Arimo", Arial, sans-serif; font-weight: 700;
    color: var(--wordmark-grey); letter-spacing: 0.04em; line-height: 1;
  }
  .wordmark__square { display: block; background: var(--accent-cyan); }
  .wordmark--large { left: 250px; top: 200px; font-size: 70px; gap: 28px; }
  .wordmark--large .wordmark__square { width: 56px; height: 56px; }
  .wordmark--small { left: 50px; top: 68px; font-size: 34px; gap: 16px; }
  .wordmark--small .wordmark__square { width: 28px; height: 28px; }

  .contact, .identity { position: absolute; color: var(--text-grey); }
  .contact { left: 58px; font-family: "Arimo", Arial, sans-serif; }
  .contact__address { position: absolute; top: 198px; font-size: 35px; white-space: nowrap; }
  .contact__lines { position: absolute; top: 302px; font-size: 27px; line-height: 32px; white-space: nowrap; }
  .identity { left: 420px; top: 195px; white-space: nowrap; }
  .identity__name { font-family: "Tinos", "Times New Roman", serif; font-size: 52px; line-height: 56px; }
  .identity__role { font-family: "Arimo", Arial, sans-serif; font-size: 26px; line-height: 30px; margin-top: -2px; }
</style>
</head>
<body>
<main class="canvas">
  <section class="card card--front" aria-label="Card front">
    <div class="card-backdrop" role="img" aria-label="Blue abstract geometric background framing the company name"></div>
    <div class="wordmark wordmark--large"><span class="wordmark__square"></span>Quorvex</div>
  </section>

  <section class="card card--back" aria-label="Card back">
    <div class="wordmark wordmark--small"><span class="wordmark__square"></span>Quorvex</div>
    <div class="contact">
      <p class="contact__address">Address</p>
      <p class="contact__lines">Phone Number<br>Email<br>&nbsp;Website</p>
    </div>
    <div class="identity">
      <p class="identity__name">Employee Name</p>
      <p class="identity__role">Postion</p>
    </div>
  </section>
</main>
</body>
</html>
```